Unique & Creative Business Card for Lumivaleta

Would you please create a unique design that is soft and appealing to people who seek to raise vibrational energy for themselves, for animals (domestic or wild), or for the environment.

Optional: Elements could include, landscapes, wild animals, feathers, vibrational patterns, the elements (Earth, water, fire, air and space). Images that are calming.

With Thanks!

Target Market(s)

People and businesses who are into the environment, animal welfare, alternative health.

Contact Information for Business Card

Moira Tess
Energist
mt@lumivaleta.example
lumivaleta.example

Requirements
Must have
• Lumivaleta logo (attached)
Symbols that represent our main services: Natural environment, animal, human and energy.
Our strapline ‘Achieving Vibrational Equilibrium’
Nice to have
• Clear and easy to read
Colours based on nature/soft colours

```html
<!DOCTYPE html>
<html lang="en">
<head>
<meta charset="utf-8">
<title>Lumivaleta Business Card</title>
<link href="https://fonts.googleapis.com/css2?family=Oswald:wght@500&family=Work+Sans:wght@400;500&display=swap" rel="stylesheet">
<style>
  :root {
    --page-bg: #2b2b2c;
    --sky-top: #5b5d60;
    --sky-warm: #6e5a55;
    --mist: #3f5a62;
    --forest: #1f3a42;
    --forest-deep: #162a30;
    --ink-light: #ffffff;
    --ink-soft: #e6ecee;
    --divider: rgba(255,255,255,0.75);
  }
  * { margin: 0; padding: 0; box-sizing: border-box; }
  html, body { width: 1200px; height: 930px; overflow: hidden; }
  body {
    background: var(--page-bg);
    font-family: "Work Sans", Arial, sans-serif;
    color: var(--ink-light);
    position: relative;
  }
  .card {
    position: absolute;
    left: 260px;
    width: 680px;
    height: 389px;
    border-radius: 22px;
    overflow: hidden;
    box-shadow: 0 14px 30px rgba(0,0,0,0.45);
  }
  .card--front { top: 55px; }
  .card--back { top: 486px; }
  .landscape {
    position: absolute;
    inset: 0;
    background:
      radial-gradient(ellipse 30% 40% at 62% 28%, rgba(140,100,88,0.55), transparent 70%),
      linear-gradient(180deg, var(--sky-top) 0%, var(--sky-warm) 28%, var(--mist) 50%, var(--forest) 72%, var(--forest-deep) 100%);
  }
  .brand {
    position: absolute;
    left: 0; right: 0;
    top: 118px;
    display: flex;
    align-items: center;
    justify-content: center;
    gap: 16px;
  }
  .brand__dot {
    width: 34px; height: 34px;
    border-radius: 50%;
    background: var(--ink-light);
  }
  .brand__name {
    font-family: "Work Sans", Arial, sans-serif;
    font-weight: 500;
    font-size: 38px;
    letter-spacing: 3px;
    text-transform: uppercase;
    color: var(--ink-light);
  }
  .strapline {
    position: absolute;
    left: 0; right: 0;
    top: 220px;
    text-align: center;
    font-size: 17px;
    line-height: 1.4;
    color: var(--ink-soft);
  }
  .identity {
    position: absolute;
    left: 150px;
    top: 168px;
    text-align: right;
  }
  .identity__name {
    font-family: "Oswald", Arial Narrow, sans-serif;
    font-weight: 500;
    font-size: 42px;
    letter-spacing: 2px;
    text-transform: uppercase;
    line-height: 1;
  }
  .identity__role {
    font-size: 18px;
    margin-top: 6px;
    color: var(--ink-soft);
  }
  .divider {
    position: absolute;
    left: 395px;
    top: 152px;
    width: 1px;
    height: 100px;
    background: var(--divider);
  }
  .contacts {
    position: absolute;
    left: 412px;
    top: 156px;
    list-style: none;
    font-size: 16px;
    line-height: 30px;
  }
  .contacts li { display: flex; align-items: center; gap: 7px; }
  .contacts svg { width: 13px; height: 13px; fill: none; stroke: var(--ink-light); stroke-width: 1.6; }
</style>
</head>
<body>
  <section class="card card--front">
    <div class="landscape" role="img" aria-label="Misty mountain valley with pine forest and a river at dusk"></div>
    <div class="brand">
      <span class="brand__dot"></span>
      <span class="brand__name">Lumivaleta</span>
    </div>
    <p class="strapline">Natural environment, animal, human and energy.<br>Our strapline ‘Achieving Vibrational Equilibrium</p>
  </section>

  <section class="card card--back">
    <div class="landscape" role="img" aria-label="Misty mountain valley with pine forest and a river at dusk"></div>
    <div class="identity">
      <h1 class="identity__name">Moira Tess</h1>
      <p class="identity__role">Energist</p>
    </div>
    <div class="divider"></div>
    <ul class="contacts">
      <li>
        <svg viewBox="0 0 16 16"><path d="M3 2h3l1.5 3.5-2 1.2a9 9 0 0 0 3.8 3.8l1.2-2L14 10v3a1 1 0 0 1-1 1A11 11 0 0 1 2 3a1 1 0 0 1 1-1z"/></svg>
        06.41.27.83.15
      </li>
      <li>
        <svg viewBox="0 0 16 16"><rect x="1.5" y="3.5" width="13" height="9" rx="1"/><path d="M1.5 4l6.5 5 6.5-5"/></svg>
        mt@lumivaleta.example
      </li>
      <li>
        <svg viewBox="0 0 16 16"><circle cx="8" cy="8" r="6.5"/><path d="M1.5 8h13M8 1.5c2.5 3 2.5 10 0 13M8 1.5c-2.5 3-2.5 10 0 13"/></svg>
        www.lumivaleta.example
      </li>
    </ul>
  </section>
</body>
</html>
```